Book Cover for Productivity Book

I need a book cover for my latest publication "On Momentum: The Gathered Insights of the Most Tireless Woman Living"

You can see my branding at www.brightvarno.com

This is meant to be my epic pinaccle work on productivity, I want it to look like the end all be all word on productivity.

Target Market(s)

entrepreneurs

```html
<!DOCTYPE html>
<html lang="en">
<head>
<meta charset="utf-8">
<title>On Momentum — Book Cover</title>
<link rel="stylesheet" href="https://fonts.googleapis.com/css2?family=Montserrat:wght@800;900&family=Raleway:wght@400;500&display=swap">
<style>
  :root {
    --backdrop: #a9d0d6;
    --cover: #050505;
    --title-light: #e6e6e6;
    --title-red: #a30505;
    --rule: #d9d9d9;
    --subtitle: #e9e9e9;
    --chalk: #3a3a3a;
    --chalk-gold: #6b5a12;
  }
  * { margin: 0; padding: 0; box-sizing: border-box; }
  html, body {
    width: 1200px;
    height: 1200px;
    overflow: hidden;
    background: var(--backdrop);
  }
  .canvas {
    position: relative;
    width: 1200px;
    height: 1200px;
    background: var(--backdrop);
  }
  .cover {
    position: absolute;
    left: 220px;
    top: 40px;
    width: 760px;
    height: 1120px;
    background: var(--cover);
    overflow: hidden;
  }
  .title {
    position: absolute;
    left: 52px;
    top: 124px;
    font-family: "Montserrat", sans-serif;
    font-weight: 900;
    line-height: 1;
  }
  .title-lead {
    display: block;
    font-size: 76px;
    color: var(--title-light);
    letter-spacing: 1px;
  }
  .title-main {
    display: block;
    margin-top: -4px;
    font-size: 104px;
    color: var(--title-red);
    letter-spacing: 1px;
  }
  .title-rule {
    position: absolute;
    left: 54px;
    top: 292px;
    width: 665px;
    height: 4px;
    background: var(--rule);
  }
  .subtitle {
    position: absolute;
    left: 0;
    top: 328px;
    width: 760px;
    text-align: center;
    font-family: "Raleway", sans-serif;
    font-weight: 500;
    font-size: 36px;
    line-height: 72px;
    color: var(--subtitle);
  }
  .illustration {
    position: absolute;
    left: 60px;
    top: 540px;
    width: 640px;
    height: 500px;
  }
</style>
</head>
<body>
  <main class="canvas">
    <section class="cover">
      <h1 class="title">
        <span class="title-lead">ON</span>
        <span class="title-main">MOMENTUM</span>
      </h1>
      <div class="title-rule"></div>
      <p class="subtitle">The Gathered Insights<br>of the Most Tireless Woman Living</p>
      <svg class="illustration" role="img" aria-label="Chalk drawing of a yellow head in profile with ideas flowing out: a clock, heart, light bulb, eye, leaves, money and notes" viewBox="0 0 640 500">
        <defs>
          <radialGradient id="chalk-glow" cx="0.5" cy="0.65" r="0.6">
            <stop offset="0" stop-color="var(--chalk-gold)"/>
            <stop offset="0.35" stop-color="var(--chalk)"/>
            <stop offset="1" stop-color="var(--cover)"/>
          </radialGradient>
        </defs>
        <rect width="640" height="500" fill="url(#chalk-glow)"/>
      </svg>
    </section>
  </main>
</body>
</html>
```